Global Nano Technology Surface Protection company needs a new logo and cards

We are a Global company that will apply nanotechnology coatings on surfaces to prevent growth and spread of bacteria, viruses, mold etc. We deal with large corporates, airlines, hospitals and schools so we are after a new modern, simple and clean look that will have great visual impact.
We a company that is focused on prevention and protection.

Company name, Quorvane Systems Worldwide

Subtext, Antimicrobial Surface Protection

Logo, QVSW or QSW

Target Market(s)

Hospitals, Transport agencies, Airlines, Corporate entities

Industry/Entity Type

Protection

Contact Information for Business Card

Logo, QVSW or QSW
www.qvsw-example.us
Derek Holloway
+64290536218
tidyshieldnz@mailbox-example.com

Logo Text

QVSW

Requirements
Must have
• Simple clean look
Should not have
• Nothing too messy

```html
<!DOCTYPE html>
<html lang="en">
<head>
<meta charset="utf-8">
<title>Quorvane Systems Worldwide – Business Cards</title>
<link rel="stylesheet" href="https://fonts.googleapis.com/css2?family=Montserrat:wght@400;500;700&display=swap">
<style>
  :root {
    --brand-red: #b01e2f;
    --ink: #111213;
    --paper: #ffffff;
    --stage: #2b2e33;
    --muted-white: #e9e9e9;
  }
  * { box-sizing: border-box; margin: 0; padding: 0; }
  html, body { width: 1200px; height: 900px; overflow: hidden; }
  body {
    background: var(--stage);
    font-family: "Montserrat", Arial, sans-serif;
    position: relative;
  }
  .card {
    position: absolute;
    overflow: hidden;
    box-shadow: 0 14px 30px rgba(0,0,0,0.45);
  }
  .card-bg { position: absolute; inset: 0; width: 100%; height: 100%; }

  /* Logo lockup */
  .logo {
    display: flex;
    align-items: center;
    gap: 10px;
  }
  .logo-square {
    width: 40px; height: 40px;
    background: var(--brand-red);
  }
  .logo-name {
    font-weight: 700;
    color: var(--brand-red);
    font-size: 40px;
    letter-spacing: 2px;
    line-height: 1;
  }

  /* Front card (portrait) */
  .card-front { left: 150px; top: 190px; width: 300px; height: 520px; }
  .card-front .logo {
    position: absolute;
    left: 0; right: 0; top: 110px;
    justify-content: center;
  }
  .contact-block {
    position: absolute;
    right: 20px;
    top: 352px;
    text-align: right;
    color: var(--paper);
  }
  .person-name {
    font-weight: 700;
    font-size: 19px;
    letter-spacing: 0.5px;
    text-transform: uppercase;
    margin-right: 26px;
  }
  .person-title {
    color: var(--brand-red);
    font-size: 13px;
    font-weight: 500;
    margin: 2px 26px 16px 0;
  }
  .contact-line {
    display: flex;
    justify-content: flex-end;
    align-items: center;
    gap: 10px;
    font-size: 11px;
    color: var(--muted-white);
    margin-bottom: 10px;
    white-space: nowrap;
  }
  .contact-icon { width: 16px; height: 16px; flex: none; }

  /* Back card (landscape) */
  .card-back { left: 560px; top: 300px; width: 520px; height: 300px; }
  .logo-panel {
    position: absolute;
    left: 120px; top: 70px;
    width: 280px; height: 160px;
    background: var(--paper);
    display: flex;
    align-items: center;
    justify-content: center;
  }
  .card-back .logo-square { width: 48px; height: 48px; }
  .card-back .logo-name { font-size: 48px; }
</style>
</head>
<body>

  <section class="card card-front" aria-label="Business card front">
    <svg class="card-bg" viewBox="0 0 300 520" preserveAspectRatio="none" aria-hidden="true">
      <rect width="300" height="520" fill="var(--paper)"/>
      <polygon points="0,318 300,240 300,520 0,520" fill="var(--brand-red)"/>
      <polygon points="0,338 300,260 300,520 0,520" fill="var(--ink)"/>
    </svg>

    <div class="logo">
      <span class="logo-square"></span>
      <span class="logo-name">QVSW</span>
    </div>

    <div class="contact-block">
      <p class="person-name">Derek Holloway</p>
      <p class="person-title">President &amp; ceo</p>
      <p class="contact-line">+64290536218
        <svg class="contact-icon" viewBox="0 0 16 16" aria-hidden="true"><rect x="4" y="1.5" width="8" height="13" rx="1.5" fill="none" stroke="var(--brand-red)" stroke-width="1.5"/></svg>
      </p>
      <p class="contact-line">tidyshieldnz@mailbox-example.com
        <svg class="contact-icon" viewBox="0 0 16 16" aria-hidden="true"><rect x="1.5" y="3.5" width="13" height="9" fill="none" stroke="var(--brand-red)" stroke-width="1.5"/><polyline points="1.5,3.5 8,9 14.5,3.5" fill="none" stroke="var(--brand-red)" stroke-width="1.5"/></svg>
      </p>
      <p class="contact-line">www.qvsw-example.us
        <svg class="contact-icon" viewBox="0 0 16 16" aria-hidden="true"><polyline points="2,8 8,2.5 14,8" fill="none" stroke="var(--brand-red)" stroke-width="1.5"/><polyline points="4,7 4,14 12,14 12,7" fill="none" stroke="var(--brand-red)" stroke-width="1.5"/></svg>
      </p>
    </div>
  </section>

  <section class="card card-back" aria-label="Business card back">
    <svg class="card-bg" viewBox="0 0 520 300" preserveAspectRatio="none" aria-hidden="true">
      <rect width="520" height="300" fill="var(--ink)"/>
      <polygon points="0,0 520,0 520,95 0,235" fill="var(--brand-red)"/>
    </svg>
    <div class="logo-panel">
      <div class="logo">
        <span class="logo-square"></span>
        <span class="logo-name">QVSW</span>
      </div>
    </div>
  </section>

</body>
</html>
```